BrookVale Collision Repair Web Site

Create a web site that will inform my potential customers about the services I provide. We are a Automotive Collision repair business that uses the latest state of the art equipment, computerized paint matching highly trained technicians, have over 30 years experience. We work with all all insurance programs. Our Moto is "Fixed Right, The First Time, Every Time". BrookVale, The trusted pick in collision repair.

Target Market(s)

People that have been in a auto collision, needs windshield replaced, people that drive 10 year or newer cars

Industry/Entity Type

Automotive

Coding

Coded - Design and coding required

Number of Pages Required

4 page

Font styles to use
Sans Serif

Requirements
Must have
• Logo, Place for Phone number, I need to be able to put the code in so I can use a tracking phone number
• site needs to be mobile ready or adaptive
• May want to have a photo of a high end car
• here is a web site for example with the pages that I want
• https://www.pondlyautobody.example/online-repair-estimate,
• https://www.pondlyautobody.example/schedule-appointment
• https://www.pondlyautobody.example/collision-repair/auto-body-repair
• https://www.pondlyautobody.example/contact
Nice to have
• Be great if the Car in the log could have the front damaged then have it fix in a animation. Not sure if could be done here

```html
<!DOCTYPE html>
<html lang="en">
<head>
<meta charset="utf-8">
<title>BrookVale Collision Repair</title>
<link rel="stylesheet" href="https://fonts.googleapis.com/css2?family=Arimo:wght@400;700&family=Archivo+Narrow:wght@400&display=swap">
<style>
:root{
  --blue:#1d4f9f;
  --blue-deep:#1a47a0;
  --blue-light:#e9eef8;
  --ink:#444;
  --ink-soft:#555;
  --green:#7ab51d;
  --green-dark:#5a8f10;
  --red:#d7262e;
  --panel:#f2f2f2;
  --white:#fff;
  --footer:#626262;
  --social:#2a5aa8;
}
*{margin:0;padding:0;box-sizing:border-box}
html,body{width:720px;height:1200px;overflow:hidden;background:var(--white)}
body{font-family:"Arimo",Arial,sans-serif;color:var(--ink)}
.page{position:relative;width:720px;height:1200px;overflow:hidden}
.abs{position:absolute}

/* header */
.header{left:0;top:0;width:720px;height:86px;background:var(--panel)}
.brand{left:74px;top:28px;display:flex;align-items:center;gap:8px}
.brand-dot{width:14px;height:14px;border-radius:50%;background:var(--green)}
.brand-name{font-size:24px;font-weight:700;color:var(--blue);letter-spacing:.3px}
.phone{right:48px;top:20px;display:flex;align-items:center;gap:6px;font-size:15px;color:var(--blue)}
.phone-icon{width:16px;height:16px;border-radius:3px;background:#5fa83a}
.social-top{right:48px;top:47px;display:flex;gap:5px}
.social-top span{width:18px;height:18px;border-radius:50%;background:var(--social)}

/* hero */
.hero{left:0;top:86px;width:720px;height:199px;background:linear-gradient(180deg,var(--blue-deep) 0%,#3a66b7 45%,#c3d0ea 85%,var(--blue-light) 100%)}
.nav{left:0;top:86px;width:720px;height:34px;display:flex;justify-content:center;align-items:center;gap:18px;color:var(--white);font-size:13px}
.nav .sep{opacity:.9}
.hero-photo{left:40px;top:134px;width:365px;height:132px;border-radius:6px;background:linear-gradient(90deg,#d9dde4,#f4f5f7 50%,#cfd4dc)}
.hero-title{left:400px;top:134px;width:315px;text-align:center;font-size:26px;font-weight:700;color:#8cc63f;letter-spacing:.5px}
.hero-tag{left:400px;top:176px;width:315px;text-align:center;font-family:"Archivo Narrow",Arial,sans-serif;font-size:17px;color:var(--white)}
.dots{left:536px;top:221px;display:flex;gap:5px}
.dots span{width:9px;height:9px;border-radius:50%;background:var(--white)}

/* services */
.services{left:0;top:285px;width:720px;height:269px;background:var(--panel)}
.section-title{font-size:19px;color:var(--blue);text-align:center;width:720px;left:0}
.services-sub{left:0;top:335px;width:720px;text-align:center;font-size:12.5px;color:var(--ink-soft)}
.service{top:366px;width:180px;text-align:center}
.service svg{display:block;margin:0 auto}
.service h3{margin-top:18px;font-size:12.5px;font-weight:400;color:var(--blue)}
.service p{margin-top:6px;font-size:9.5px;line-height:10.5px;color:var(--ink)}
.btn-green{display:inline-block;margin-top:15px;width:64px;height:21px;line-height:21px;border-radius:3px;background:linear-gradient(180deg,#8fce2a,var(--green-dark));color:var(--white);font-size:7px;font-weight:700;box-shadow:0 1px 2px rgba(0,0,0,.35)}

/* welcome */
.welcome-title{left:97px;top:584px;font-size:16px;font-weight:700;color:var(--blue)}
.welcome-text{left:96px;top:613px;width:344px;font-size:9.7px;line-height:12px;color:var(--ink)}
.btn-blue{left:97px;top:694px;width:61px;height:21px;line-height:21px;text-align:center;border-radius:3px;background:var(--blue);color:var(--white);font-size:8.5px}
.car-photo{left:456px;top:582px;width:264px;height:114px;border-radius:40px 10px 6px 30px;background:linear-gradient(180deg,#c3262e,#9d1a20 60%,#e8e8e8)}

/* why */
.why{left:0;top:739px;width:720px;height:376px;background:var(--panel)}
.why-title{left:90px;top:765px;font-size:12.5px;font-weight:700;color:var(--blue)}
.why-list{left:94px;top:788px;width:350px;list-style:none;font-size:9.7px;line-height:12px;color:var(--ink)}
.why-list li{margin-bottom:5px}
.why-list li::before{content:"\25CF";font-size:6px;margin-right:6px;vertical-align:2px}
.divider{left:463px;top:788px;width:1px;height:130px;background:#bbb}
.quick{left:478px;display:flex;align-items:center;gap:14px;font-size:10px;color:var(--ink)}

/* testimonials */
.quote{left:160px;top:978px;width:420px;text-align:center;font-size:9.7px;line-height:12px;color:var(--ink)}
.qmark{font-family:Georgia,serif;font-size:34px;color:#bbb}
.arrow{font-size:26px;color:#777}
.avatar{left:263px;top:1033px;width:48px;height:48px;border-radius:50%;background:var(--blue-deep)}
.author{left:333px;top:1045px;font-size:10px;color:var(--red)}
.author-sub{left:333px;top:1062px;font-size:10px;color:var(--ink)}

/* footer */
.footer{left:0;top:1115px;width:720px;height:85px;background:var(--footer)}
.copyright{left:87px;top:1151px;font-size:15px;color:var(--white)}
.social-foot{left:469px;top:1143px;display:flex;gap:9px}
.social-foot span{width:30px;height:30px;border-radius:50%;background:var(--social);border:2px solid #8a8a8a}
</style>
</head>
<body>
<div class="page">

  <header class="abs header"></header>
  <div class="abs brand"><span class="brand-dot"></span><span class="brand-name">BrookVale</span></div>
  <div class="abs phone"><span class="phone-icon"></span>1-555-0142</div>
  <div class="abs social-top" aria-label="Social links"><span></span><span></span><span></span><span></span><span></span></div>

  <section class="abs hero"></section>
  <nav class="abs nav">
    <span>Home</span><span class="sep">|</span><span>About Us</span><span class="sep">|</span><span>Services</span><span class="sep">|</span><span>FAQ</span><span class="sep">|</span><span>Testimonials</span><span class="sep">|</span><span>Contact</span>
  </nav>
  <div class="abs hero-photo" role="img" aria-label="Before and after photos of a white sedan with front collision damage and the same car repaired"></div>
  <div class="abs hero-title">BROOKVALE</div>
  <div class="abs hero-tag">The trusted pick in Collision Repair</div>
  <div class="abs dots"><span></span><span></span><span></span></div>

  <section class="abs services"></section>
  <h2 class="abs section-title" style="top:302px">Our Services</h2>
  <p class="abs services-sub">Lorem ipsum dolor sit amet, consectetur adipiscing elit, sed do eiusmod tempor</p>

  <div class="abs service" style="left:75px">
    <svg width="66" height="66" viewBox="0 0 66 66"><circle cx="33" cy="33" r="29" fill="none" stroke="#1d4f9f" stroke-width="5"/>
      <path d="M20 34 L24 24 H42 L46 34 V44 H20 Z" fill="#1d4f9f"/><rect x="26" y="27" width="14" height="6" fill="#fff"/><circle cx="25" cy="38" r="2" fill="#fff"/><circle cx="41" cy="38" r="2" fill="#fff"/><rect x="21" y="44" width="5" height="4" fill="#1d4f9f"/><rect x="40" y="44" width="5" height="4" fill="#1d4f9f"/></svg>
    <h3>COLLISION REPAIR</h3>
    <p>Lorem ipsum dolor sit amet,-<br>consectetur adipiscing elit, sed</p>
    <span class="btn-green">READ MORE</span>
  </div>
  <div class="abs service" style="left:268px">
    <svg width="66" height="66" viewBox="0 0 66 66"><circle cx="33" cy="33" r="29" fill="none" stroke="#1d4f9f" stroke-width="5"/>
      <path d="M22 46 L38 30" stroke="#1d4f9f" stroke-width="6" stroke-linecap="round"/><circle cx="41" cy="26" r="7" fill="#1d4f9f"/><path d="M42 19 L46 23 L44 27 L40 25 Z" fill="#fff"/></svg>
    <h3>FRAME REPAIR</h3>
    <p>Lorem ipsum dolor sit amet,-<br>consectetur adipiscing elit, sed</p>
    <span class="btn-green">READ MORE</span>
  </div>
  <div class="abs service" style="left:460px">
    <svg width="66" height="66" viewBox="0 0 66 66"><circle cx="33" cy="33" r="29" fill="none" stroke="#1d4f9f" stroke-width="5"/>
      <path d="M17 40 L20 30 H32 V44 H17 Z" fill="#1d4f9f"/><rect x="36" y="22" width="4" height="22" fill="#1d4f9f"/><rect x="43" y="22" width="4" height="22" fill="#1d4f9f"/><rect x="36" y="31" width="11" height="3" fill="#1d4f9f"/></svg>
    <h3>ALIGNMENT</h3>
    <p>Lorem ipsum dolor sit amet,-<br>consectetur adipiscing elit, sed</p>
    <span class="btn-green">READ MORE</span>
  </div>

  <h2 class="abs welcome-title">Welcome to BrookVale Collision Repair</h2>
  <p class="abs welcome-text">For over 30 years’ vehicle owners and fleet managers have trusted our staff for all their collision repairs. Our Nationwide, Lifetime Guarantee and excellent customer service are just a few of the reasons you want to choose BrookVale. We use the latest computerized frame alignment and paint matching technology. Our professional staff of certified technicians take pride in the work they do and strive to deliver the best possible service.</p>
  <div class="abs btn-blue">Read More</div>
  <div class="abs car-photo" role="img" aria-label="Photo of a red high-end sports coupe"></div>

  <section class="abs why"></section>
  <h2 class="abs why-title">Why is BrookVale the Trusted Pick in Collision Repair?</h2>
  <ul class="abs why-list">
    <li>We ensure that latest OEM approved procedures are followed during each phase of the repair of your vehicle.</li>
    <li>We have the latest in computerized frame equipment.</li>
    <li>Our technicians are certified in structural repairs ensuring that your vehicle will be as safe for your family as it was the day it left the factory.</li>
    <li>Our refinish equipment and trained painters will make sure your finish is back to factory finish maybe even better.</li>
    <li>Each repair including paint and collision repair comes with a limited lifetime warranty as long as you own the vehicle.</li>
  </ul>
  <div class="abs divider"></div>
  <div class="abs quick" style="top:790px">
    <svg width="26" height="26" viewBox="0 0 26 26"><rect x="2" y="4" width="20" height="18" rx="2" fill="none" stroke="#1d4f9f" stroke-width="2"/><rect x="2" y="4" width="20" height="5" fill="#1d4f9f"/><circle cx="20" cy="20" r="5" fill="#fff" stroke="#1d4f9f" stroke-width="1.5"/><path d="M20 17 V20 H22" stroke="#1d4f9f" stroke-width="1.2" fill="none"/></svg>
    <span>Schedule an Appointment</span></div>
  <div class="abs quick" style="top:825px">
    <svg width="26" height="26" viewBox="0 0 26 26"><rect x="4" y="3" width="16" height="20" fill="none" stroke="#1d4f9f" stroke-width="2"/><path d="M8 9 H16 M8 13 H14" stroke="#1d4f9f" stroke-width="1.5"/><path d="M12 20 L22 10 L24 12 L14 22 Z" fill="#1d4f9f"/></svg>
    <span>Online Estimate</span></div>
  <div class="abs quick" style="top:861px">
    <svg width="26" height="26" viewBox="0 0 26 26"><path d="M4 14 A9 9 0 0 1 22 14" fill="none" stroke="#1d4f9f" stroke-width="2.5"/><rect x="2" y="13" width="5" height="7" rx="2" fill="#1d4f9f"/><rect x="19" y="13" width="5" height="7" rx="2" fill="#1d4f9f"/><path d="M21 20 Q21 24 15 24" fill="none" stroke="#1d4f9f" stroke-width="1.5"/></svg>
    <span>Customer Care</span></div>

  <h2 class="abs section-title" style="top:945px">Testimonials</h2>
  <span class="abs qmark" style="left:120px;top:966px">“</span>
  <p class="abs quote">Lorem ipsum dolor sit amet, consectetur adipiscing elit, sed do eiusmod tempor Ut enim ad minim veniam, quis nostrud exercitation ullamco laboris nisi ut aliquip ex ea commodo consequat.</p>
  <span class="abs qmark" style="left:598px;top:972px">”</span>
  <span class="abs arrow" style="left:227px;top:1040px">&lt;</span>
  <div class="abs avatar"></div>
  <svg class="abs" style="left:275px;top:1043px" width="24" height="28" viewBox="0 0 24 28"><circle cx="12" cy="7" r="5" fill="#fff"/><rect x="4" y="14" width="16" height="13" rx="5" fill="#fff"/></svg>
  <div class="abs author">By Dana Whitfield</div>
  <div class="abs author-sub">Lorem ipsum dolor sit amet</div>
  <span class="abs arrow" style="left:472px;top:1040px">&gt;</span>

  <footer class="abs footer"></footer>
  <div class="abs copyright">Copyright @ BrookVale 2016</div>
  <div class="abs social-foot" aria-label="Social links"><span></span><span></span><span></span><span></span><span></span></div>

</div>
</body>
</html>
```